New Solo Law Office Needs Business Card/Letterhead Design

I am starting a solo law office called "Law Office of Brian Kolmer, PLLC" in Tucson, Arizona. I will be doing criminal defense trial work. More than a logo with any sort of icon, I am really just looking for the name of the company to be displayed in a sleek, minimalist but interesting sort of way, with a format and font type that communicates professionalism. It can be in color, but doesn't have to be, and I am thinking blue and/or red accents colors. I'd like it to convey that I am passionate, dependable and willing to fight. For the business card, I envision sort of higher quality card material, and maybe some embossing or raised print. I will want to include my company name, name, phone and fax numbers, email and website addresses. For the letterhead, I will want to be able to use the same sort of font/formatting design as on the business card.
Industry/Entity Type
Business
Contact Information for Business Card
Law Office of Brian Kolmer, PLLC
Brian Kolmer
brian@kolmer-law.example
www.kolmer-law.example
(I do not yet have an established phone or fax number, so please put in some place holder numbers for the formatting, and I can add the actual numbers in before I print.)
Colors
Designer to choose colors to be used in the design.
Look and feel
Each slider illustrates characteristics of the customer's brand and the style your logo design should communicate.

```html
<!DOCTYPE html>
<html lang="en">
<head>
<meta charset="utf-8">
<title>Law Office of Brian Kolmer, PLLC — Business Card</title>
<link href="https://fonts.googleapis.com/css2?family=Cormorant+SC:wght@500&family=Lato:wght@400&display=swap" rel="stylesheet">
<style>
  :root {
    --navy: #1b1a5e;
    --ink: #2f2f3a;
    --grey: #55555f;
    --paper: #f7f7f8;
    --backdrop: #e9e6e1;
    --on-navy: #ffffff;
  }
  * { box-sizing: border-box; margin: 0; padding: 0; }
  html, body { width: 1200px; height: 800px; overflow: hidden; }
  body {
    background: var(--backdrop);
    font-family: "Lato", sans-serif;
    position: relative;
  }
  .card {
    position: absolute;
    width: 520px;
    height: 300px;
    top: 250px;
    box-shadow: 0 6px 18px rgba(0,0,0,0.18);
    overflow: hidden;
  }
  .card--front { left: 50px; background: var(--navy); color: var(--on-navy); }
  .card--back  { left: 630px; background: var(--paper); color: var(--navy); }

  .firm {
    position: absolute;
    display: flex;
    align-items: center;
    gap: 16px;
  }
  .firm__rule { width: 1px; align-self: stretch; }
  .firm__name {
    font-family: "Cormorant SC", serif;
    font-weight: 500;
    line-height: 1.0;
  }
  .firm__dot { width: 14px; height: 14px; border-radius: 50%; flex: none; }

  .card--front .firm { left: 120px; top: 98px; }
  .card--front .firm__rule { background: var(--on-navy); }
  .card--front .firm__name { font-size: 29px; color: var(--on-navy); }
  .card--front .firm__dot { background: var(--on-navy); }

  .address {
    position: absolute;
    right: 34px;
    bottom: 30px;
    font-size: 13px;
    letter-spacing: 0.3px;
  }

  .card--back .firm { left: 40px; top: 34px; }
  .card--back .firm__rule { background: var(--ink); }
  .card--back .firm__name { font-size: 24px; color: var(--navy); }
  .card--back .firm__dot { background: var(--navy); }

  .person { position: absolute; left: 40px; top: 130px; }
  .person__name {
    font-family: "Cormorant SC", serif;
    font-weight: 500;
    font-size: 23px;
    color: var(--navy);
    line-height: 1;
  }
  .person__title { font-size: 14px; color: var(--grey); margin-top: 2px; }

  .divider {
    position: absolute;
    left: 40px;
    right: 40px;
    top: 186px;
    height: 1px;
    background: var(--navy);
  }

  .contacts { position: absolute; list-style: none; font-size: 13px; color: var(--ink); }
  .contacts li { display: flex; align-items: center; gap: 10px; height: 21px; }
  .contacts svg { width: 13px; height: 13px; fill: var(--navy); flex: none; }
  .contacts--phones { left: 40px; top: 200px; }
  .contacts--web { right: 40px; top: 232px; }

  .band {
    position: absolute;
    left: 0; right: 0; bottom: 0;
    height: 18px;
    background: var(--navy);
  }
</style>
</head>
<body>

  <section class="card card--front" aria-label="Business card, front">
    <div class="firm">
      <span class="firm__dot"></span>
      <span class="firm__rule"></span>
      <span class="firm__name">Law Office of<br>Brian Kolmer, PLLC</span>
    </div>
    <p class="address">Level 2, 48 Placeholder Street, Tucson AZ</p>
  </section>

  <section class="card card--back" aria-label="Business card, back">
    <div class="firm">
      <span class="firm__dot"></span>
      <span class="firm__rule"></span>
      <span class="firm__name">Law Office of<br>Brian Kolmer, PLLC</span>
    </div>

    <div class="person">
      <p class="person__name">Brian Kolmer</p>
      <p class="person__title">Attorney At Law</p>
    </div>

    <div class="divider"></div>

    <ul class="contacts contacts--phones">
      <li>
        <svg viewBox="0 0 16 16" aria-label="Fax"><rect x="4" y="1" width="8" height="5"/><rect x="1" y="6" width="14" height="7" rx="1"/><rect x="4" y="11" width="8" height="4" fill="#fff"/></svg>
        555 010 4821
      </li>
      <li>
        <svg viewBox="0 0 16 16" aria-label="Phone"><path d="M3.5 1 6 1.5 7 5 5.3 6.4a9 9 0 0 0 4.3 4.3L11 9l3.5 1 .5 2.5-2 2C7 14.5 1.5 9 1.5 3z"/></svg>
        555 010 7730
      </li>
    </ul>

    <ul class="contacts contacts--web">
      <li>
        <svg viewBox="0 0 16 16" aria-label="Website"><path d="M1 3h14v10H1z"/><path d="M1 3l7 6 7-6" fill="none" stroke="#fff" stroke-width="1.3"/></svg>
        www.kolmer-law.example
      </li>
      <li>
        <svg viewBox="0 0 16 16" aria-label="Email"><circle cx="8" cy="8" r="7"/><path d="M1 8h14M8 1c-3 3.5-3 10.5 0 14M8 1c3 3.5 3 10.5 0 14" fill="none" stroke="#fff" stroke-width="1"/></svg>
        brian@kolmer-law.example
      </li>
    </ul>

    <div class="band"></div>
  </section>

</body>
</html>
```